Building Asset Management and Engineering Services for complex buildings

We provide asset management, project management, and engineering services for complex buildings.
Asset management services include, asset management strategies, plans, risk and conditioning assessments.
The engineering services include building services redesign, project management and commissioning services.

Target Market(s)

architects, government, electrical contractors

Industry/Entity Type

Asset Management

Contact Information for Business Card

KLT van Brommel QTSph, MKOrvia, DGLT, SMVK
Director
Other details such as address please refer to attached file

Font styles to use
Sans Serif

Requirements
Must have
• Fellow and Engineers logo on the back
• * Strategic Planning
• * Design
• * Documentation
• * Project Management
• * Commissioning
• * Assessment/Review
• Must have Engineers logo and wording on the back as well
Nice to have
• Good use of all the logo colours

```html
<!DOCTYPE html>
<html lang="en">
<head>
<meta charset="utf-8">
<title>Norvane Consultants – Business Card</title>
<link rel="stylesheet" href="https://fonts.googleapis.com/css2?family=Open+Sans:wght@400;600;700&display=swap">
<style>
  :root {
    --page-bg: #ece9e4;
    --sky-blue: #4f93c9;
    --navy: #0c1f55;
    --brand-blue: #4a8fc8;
    --ink: #2b2b2b;
    --name-navy: #1a2a5c;
    --badge-grey: #c9ced6;
  }
  * { margin: 0; padding: 0; box-sizing: border-box; }
  html, body { width: 1200px; height: 800px; overflow: hidden; }
  body {
    background: var(--page-bg);
    font-family: "Open Sans", Arial, sans-serif;
    position: relative;
  }
  .business-card {
    position: absolute;
    left: 280px;
    width: 640px; height: 366px;
    overflow: hidden;
    box-shadow: 0 8px 22px rgba(0,0,0,0.18);
  }
  .card-front { top: 16px; }
  .card-back { top: 418px; }
  .card-shapes { position: absolute; inset: 0; width: 640px; height: 366px; }

  .brand {
    position: absolute;
    left: 48px; top: 70px;
    display: flex; align-items: center; gap: 13px;
  }
  .brand-dot {
    width: 44px; height: 44px; border-radius: 50%;
    background: var(--brand-blue);
  }
  .brand-name {
    font-size: 32px; font-weight: 600; line-height: 1;
    color: var(--brand-blue);
  }

  .contact-block {
    position: absolute;
    left: 48px; top: 170px;
    color: var(--ink);
  }
  .person-name { font-size: 19px; font-weight: 700; color: var(--name-navy); line-height: 1.3; }
  .person-credentials { font-size: 12px; font-weight: 600; color: var(--name-navy); line-height: 1.4; }
  .person-title { font-size: 17px; font-weight: 400; line-height: 1.4; margin-bottom: 12px; }
  .address { font-size: 13px; margin-bottom: 4px; }
  .contact-grid {
    display: grid;
    grid-template-columns: auto auto;
    column-gap: 20px; row-gap: 4px;
    font-size: 13px;
  }
  .contact-item { display: flex; align-items: center; gap: 6px; white-space: nowrap; }
  .contact-item svg { width: 12px; height: 12px; fill: var(--name-navy); flex: none; }

  .back-brand { top: 40px; }
  .service-list {
    position: absolute;
    left: 48px; top: 116px;
    list-style: none;
    display: grid;
    grid-template-columns: 200px 200px;
    row-gap: 10px;
    font-size: 15px; color: var(--name-navy);
  }
  .service-list li { display: flex; align-items: center; gap: 9px; }
  .service-list li::before {
    content: ""; width: 8px; height: 8px; background: var(--sky-blue); flex: none;
  }
  .badges {
    position: absolute;
    left: 48px; top: 250px;
    display: flex; gap: 20px;
  }
  .badge-fellow {
    width: 62px; height: 62px; border-radius: 50%;
    background: var(--badge-grey);
  }
  .badge-engineers {
    width: 62px; height: 62px; border-radius: 8px;
    background: var(--name-navy);
  }
</style>
</head>
<body>
  <section class="business-card card-front">
    <svg class="card-shapes" viewBox="0 0 900 514" aria-hidden="true">
      <defs>
        <radialGradient id="cardFace" cx="0.45" cy="0.35" r="0.75">
          <stop offset="0" stop-color="#ffffff"/>
          <stop offset="1" stop-color="#dfe1e5"/>
        </radialGradient>
      </defs>
      <rect width="900" height="514" fill="var(--sky-blue)"/>
      <path d="M0 0 H790 C860 200 810 430 680 514 H0 Z" fill="#ffffff"/>
      <path d="M0 0 H784 C852 200 802 428 668 514 H0 Z" fill="var(--navy)"/>
      <path d="M0 0 H784 C840 170 800 380 560 514 H0 Z" fill="url(#cardFace)"/>
    </svg>

    <div class="brand">
      <span class="brand-dot"></span>
      <span class="brand-name">Norvane Consultants</span>
    </div>

    <div class="contact-block">
      <p class="person-name">KLT van Brommel</p>
      <p class="person-credentials">QTSph, MKOrvia, DGLT, SMVK</p>
      <p class="person-title">Director</p>
      <p class="address">27 Level 9, Harbour Line Road NKV</p>
      <div class="contact-grid">
        <span class="contact-item">
          <svg viewBox="0 0 24 24"><path d="M6.6 10.8a15 15 0 0 0 6.6 6.6l2.2-2.2a1 1 0 0 1 1-.25 11.4 11.4 0 0 0 3.6.57 1 1 0 0 1 1 1V20a1 1 0 0 1-1 1A17 17 0 0 1 3 4a1 1 0 0 1 1-1h3.5a1 1 0 0 1 1 1c0 1.25.2 2.45.57 3.57a1 1 0 0 1-.25 1z"/></svg>
          014 982 3310
        </span>
        <span class="contact-item">
          <svg viewBox="0 0 24 24"><path d="M2 5h20v14H2z M2 5l10 8 10-8" fill="none" stroke="#1a2a5c" stroke-width="2"/></svg>
          mail@norvane.com
        </span>
        <span class="contact-item">
          <svg viewBox="0 0 24 24"><path d="M6 2h9v6H6z M3 9h18v10H3z M7 13h10v2H7z"/></svg>
          014 982 3311
        </span>
        <span class="contact-item">
          <svg viewBox="0 0 24 24"><circle cx="12" cy="12" r="9" fill="none" stroke="#1a2a5c" stroke-width="2"/><path d="M3 12h18M12 3c3 3 3 15 0 18M12 3c-3 3-3 15 0 18" fill="none" stroke="#1a2a5c" stroke-width="1.6"/></svg>
          www.norvaneconsult.com
        </span>
      </div>
    </div>
  </section>

  <section class="business-card card-back">
    <svg class="card-shapes" viewBox="0 0 900 514" aria-hidden="true">
      <defs>
        <radialGradient id="cardBackFace" cx="0.4" cy="0.4" r="0.75">
          <stop offset="0" stop-color="#ffffff"/>
          <stop offset="1" stop-color="#dfe1e5"/>
        </radialGradient>
      </defs>
      <rect width="900" height="514" fill="var(--sky-blue)"/>
      <path d="M0 0 H790 C860 200 810 430 680 514 H0 Z" fill="#ffffff"/>
      <path d="M0 0 H784 C852 200 802 428 668 514 H0 Z" fill="var(--navy)"/>
      <path d="M0 0 H784 C840 170 800 380 560 514 H0 Z" fill="url(#cardBackFace)"/>
    </svg>

    <div class="brand back-brand">
      <span class="brand-dot"></span>
      <span class="brand-name">Norvane Consultants</span>
    </div>

    <ul class="service-list">
      <li>Strategic Planning</li>
      <li>Project Management</li>
      <li>Design</li>
      <li>Commissioning</li>
      <li>Documentation</li>
      <li>Assessment/Review</li>
    </ul>

    <div class="badges">
      <span class="badge-fellow" role="img" aria-label="Fellow membership badge"></span>
      <span class="badge-engineers" role="img" aria-label="Engineers membership badge"></span>
    </div>
  </section>
</body>
</html>
```